Web Page Color Scheme

I need the colors chosen for all of the elements in a B2B web application page (screenshot attached).

We have a web application that serves businesses (not consumers), generally Corvane 300 companies. The pages are fully developed/functional. What I want is to improve the look and feel so that the page has a more premium feel. That is the entire goal, to make the pages have a very premium feel to them. I don’t know if it is the best analogy but if you think of Varn or Pallisene as average and KTR or Osprin as premium, we want users to get a very premium feel the first time they see the screens.

What I am looking for right now is just colors. Below I describe the details.

#1 Improve the colors

The color scheme is blue and yellow. Black, gray and white are also used. I do not think the base colors should change (that is, I think we will continue to use blue and yellow) but I do think which hues, shades, tints or tones of blue, yellow and gray we use could benefit from some improvement. Feel free to use any blues, yellows and grays you think look best, lighter or darker colors, etc. You can also feel free to change what colors are used where. One note, aqua blue does not look premium. It might be deco looking or otherwise good for some things but I don’t think you will see an aqua colored Hollaway driving down the street any time soon.

Quill products tend to have a premium feel but I don’t think I am looking for a stark white appearance.

I want every color defined including but not necessarily limited to:

Backgrounds

Page Header
Navigation Panel
Page Body
Table Header
Table Header Button (the Add button)
Table Column Header
Table Rows (maybe alternating, maybe not)
Checkboxes
Table Footer

Not all of these have to be different. I assume some will be the same. I just need each carefully
thought through.

Fonts

Page Header
Navigation Panel
Page Title
Table Header Title
Table Header Button
Table Column Header
Table Row
Table Footer

Icons

Page Header
Navigation Panel
Table expander/collapse
Actions
Table Footer

Target Market(s)

Corvane 300/Pinnacle 1200

Requirements
Must have
• Premium feel

```html
<!DOCTYPE html>
<html lang="en">
<head>
<meta charset="utf-8">
<title>Data Sources – Admin Console</title>
<link href="https://fonts.googleapis.com/css2?family=Lato:wght@300;400;700&display=swap" rel="stylesheet">
<style>
:root{
  --brand-blue:#1d416b;
  --table-blue:#24507f;
  --btn-navy:#10243d;
  --gold:#e9b949;
  --gold-deep:#d9a636;
  --gold-title:#f0c25a;
  --sidebar:#2b3342;
  --workspace:#1c2029;
  --nav-active:#141820;
  --nav-hover:#46556f;
  --nav-text:#f4f5f7;
  --nav-sub:#c9ced8;
  --col-text:#1b2a40;
  --row-text:#3a4150;
  --row-line:#e4e7ec;
  --row-zebra:#f8f9fb;
  --footer:#eef0f4;
  --white:#ffffff;
}
*{box-sizing:border-box;margin:0;padding:0}
html,body{width:1200px;height:1040px;overflow:hidden;background:#fff;font-family:'Lato',sans-serif}
.app-card{position:absolute;left:51px;top:86px;width:1101px;height:842px;border-radius:32px 32px 0 32px;overflow:hidden;background:var(--workspace);box-shadow:-10px 18px 26px rgba(0,0,0,.22)}
.topbar{position:absolute;left:0;top:0;width:100%;height:91px;background:var(--brand-blue);color:#fff}
.brand{position:absolute;left:27px;top:36px;font-size:25px;font-weight:700;letter-spacing:.3px;line-height:28px}
.menu-toggle{position:absolute;left:258px;top:40px}
.topbar-tools{position:absolute;top:36px;left:724px;display:flex;gap:14px;align-items:center}
.user-menu{position:absolute;left:995px;top:40px;font-size:13px;font-weight:700}
.sidebar{position:absolute;left:0;top:91px;width:291px;bottom:0;background:var(--sidebar)}
.nav-item{position:absolute;left:0;width:291px;height:38px;display:flex;align-items:center;color:var(--nav-text);font-size:18px;font-weight:400}
.nav-item svg{position:absolute;left:26px}
.nav-item .label{position:absolute;left:60px}
.nav-item.sub .label{left:78px;font-weight:300;color:var(--nav-sub);font-size:17px}
.nav-item.sub-icon svg{left:52px}
.nav-item.sub-icon .label{left:78px;font-weight:300;font-size:17px}
.nav-item.active{background:var(--nav-active);color:var(--gold-title);border-left:4px solid var(--gold)}
.nav-item.active svg{left:22px}
.nav-item.active .label{left:56px}
.nav-item.hover{background:var(--nav-hover)}
.cursor{position:absolute;left:256px;top:493px}
.page-title{position:absolute;left:346px;top:102px;font-size:23px;font-weight:700;color:var(--gold-title)}
.search{position:absolute;left:897px;top:102px;width:180px;height:22px;background:#fff;border-radius:2px}
.search-btn{position:absolute;right:0;top:0;width:23px;height:22px;background:var(--gold);display:flex;align-items:center;justify-content:center}
.panel{position:absolute;left:307px;top:134px;width:770px;height:676px}
.block{position:absolute;background:var(--white)}
.band{height:38px;background:var(--table-blue);color:#fff;display:flex;align-items:center;font-size:18px;font-weight:400}
.add-btn{display:inline-block;background:var(--btn-navy);color:#fff;font-size:13px;border-radius:12px;padding:3px 11px;margin-left:10px}
.col-head{display:grid;height:28px;background:var(--gold);color:var(--col-text);font-size:13px;align-items:center}
.col-head>div{height:100%;display:flex;align-items:center;padding-left:10px;border-left:1px solid rgba(255,255,255,.55)}
.col-head>div:first-child{border-left:0}
.row{display:grid;height:24px;border-bottom:1px solid var(--row-line);font-size:13px;color:var(--row-text);align-items:center;background:var(--white)}
.row.zebra{background:var(--row-zebra)}
.row>div{height:100%;display:flex;align-items:center;padding-left:10px;border-left:1px solid var(--row-line)}
.row>div:first-child,.row>div.nb{border-left:0}
.row .exp{justify-content:center;padding-left:0}
.row .act{justify-content:flex-end;gap:14px;padding-right:8px}
.row .count{justify-content:flex-end;padding-right:12px}
.ds-grid{grid-template-columns:38px 174px 175px 195px 188px}
.do-grid{grid-template-columns:33px 636px 68px}
.fl-grid{grid-template-columns:211px 152px 96px 189px 55px}
.fl-grid.row{height:25.4px}
.rule-icons{justify-content:flex-end;gap:9px;padding-right:8px}
.pk{justify-content:center;padding-left:0!important}
.checkbox{width:13px;height:13px;border:1.5px solid var(--gold-deep);background:#fff;display:flex;align-items:center;justify-content:center}
.footer{position:absolute;left:0;top:639px;width:770px;height:37px;background:var(--footer);display:flex;align-items:center}
.records{position:absolute;left:33px;font-size:8px;color:#4a5262;display:flex;align-items:center;gap:3px}
.page-size{border:1px solid #9aa3b0;background:#fff;font-size:8px;padding:0 3px;display:flex;gap:6px;align-items:center}
.pager{position:absolute;left:394px;display:flex;align-items:center;gap:8px}
.page-num{width:15px;height:15px;background:var(--gold);color:var(--col-text);font-size:9px;display:flex;align-items:center;justify-content:center}
</style>
</head>
<body>
<svg width="0" height="0" style="position:absolute">
  <defs>
    <symbol id="i-expand" viewBox="0 0 14 14"><circle cx="7" cy="7" r="7" fill="#2f4563"/><path d="M5.5 4 L9.8 7 L5.5 10Z" fill="#fff"/></symbol>
    <symbol id="i-collapse" viewBox="0 0 14 14"><circle cx="7" cy="7" r="7" fill="#2f4563"/><path d="M4 5.6 L7 9.6 L10 5.6Z" fill="#fff"/></symbol>
    <symbol id="i-edit" viewBox="0 0 18 15"><rect x="1" y="1" width="13" height="12" fill="none" stroke="#3d4d66" stroke-width="1.3"/><path d="M3.5 4.5h7M3.5 7h5M3.5 9.5h4" stroke="#3d4d66" stroke-width="1"/><path d="M10 12 L16 6 L17.5 7.5 L11.5 13.5 L9.8 13.8Z" fill="#fff" stroke="#3d4d66" stroke-width="1.1"/></symbol>
    <symbol id="i-trash" viewBox="0 0 10 12"><path d="M1 2.5h8M3.5 2.5V1h3v1.5" fill="none" stroke="#d9a636" stroke-width="1"/><rect x="1.8" y="3.2" width="6.4" height="8" rx="1" fill="none" stroke="#d9a636" stroke-width="1"/><path d="M4 5v4M6 5v4" stroke="#d9a636" stroke-width=".8"/></symbol>
    <symbol id="i-at" viewBox="0 0 16 14"><circle cx="6" cy="8" r="5" fill="none" stroke="#2a3950" stroke-width="1.6"/><circle cx="6" cy="8" r="1.8" fill="#2a3950"/><path d="M8 4 L10 6 L15 1" fill="none" stroke="#2a3950" stroke-width="1.6"/></symbol>
    <symbol id="i-search" viewBox="0 0 14 14"><circle cx="6" cy="6" r="4.3" fill="none" stroke="#2a3950" stroke-width="1.3"/><path d="M9 9 L12.5 12.5" stroke="#2a3950" stroke-width="1.6"/></symbol>
    <symbol id="i-copy" viewBox="0 0 14 14"><rect x="4.5" y="1.5" width="8" height="8" fill="none" stroke="#2a3950" stroke-width="1.1"/><rect x="1.5" y="4.5" width="8" height="8" fill="#fff" stroke="#2a3950" stroke-width="1.1"/></symbol>
    <symbol id="i-fork" viewBox="0 0 14 14"><path d="M7 13V6M7 6 L3 3M7 6 L11 3" fill="none" stroke="#2a3950" stroke-width="1.2"/><circle cx="3" cy="2.5" r="1.5" fill="none" stroke="#2a3950"/><circle cx="11" cy="2.5" r="1.5" fill="none" stroke="#2a3950"/></symbol>
    <symbol id="i-globe" viewBox="0 0 14 14"><circle cx="7" cy="7" r="6" fill="#2a3950"/><path d="M1 7h12M7 1v12M3 3.5c2 1.2 6 1.2 8 0M3 10.5c2-1.2 6-1.2 8 0" fill="none" stroke="#fff" stroke-width=".9"/><ellipse cx="7" cy="7" rx="2.6" ry="6" fill="none" stroke="#fff" stroke-width=".9"/></symbol>
    <symbol id="i-list" viewBox="0 0 14 14"><path d="M1 2h12M5 5.5h8M5 8.5h8M1 12h12" stroke="#2a3950" stroke-width="1.6"/><path d="M1 4.5 L3.5 7 L1 9.5Z" fill="#2a3950"/></symbol>
    <symbol id="i-tick" viewBox="0 0 12 12"><path d="M2 6.5 L5 9 L10 2.5" fill="none" stroke="#2a3950" stroke-width="1.6"/></symbol>
  </defs>
</svg>

<div class="app-card">
  <header class="topbar">
    <div class="brand">COMPANY LOGO</div>
    <svg class="menu-toggle" width="22" height="18" viewBox="0 0 22 18"><path d="M0 2h22M0 9h22M0 16h22" stroke="#fff" stroke-width="2.2"/></svg>
    <div class="topbar-tools">
      <svg width="28" height="26" viewBox="0 0 28 26"><path d="M4 21 A11 11 0 1 1 24 21" fill="none" stroke="#fff" stroke-width="2.6"/><path d="M14 17 L19 9" stroke="#fff" stroke-width="2.4"/><circle cx="14" cy="17" r="2.2" fill="#fff"/><path d="M7 12h2M14 6v2M21 12h-2" stroke="#fff" stroke-width="2"/></svg>
      <svg width="26" height="26" viewBox="0 0 26 26"><g fill="#fff"><circle cx="13" cy="13" r="8"/><rect x="11" y="1" width="4" height="24"/><rect x="1" y="11" width="24" height="4"/><rect x="11" y="1" width="4" height="24" transform="rotate(45 13 13)"/><rect x="11" y="1" width="4" height="24" transform="rotate(-45 13 13)"/></g><circle cx="13" cy="13" r="3.5" fill="#1d416b"/></svg>
      <svg width="28" height="26" viewBox="0 0 28 26" style="margin-left:14px"><path d="M4 23 L18 9" stroke="#fff" stroke-width="3"/><path d="M20 2v5M17.5 4.5h5M24 9v4M22 11h4M15 3v3M13.5 4.5h3" stroke="#fff" stroke-width="1.6"/></svg>
      <svg width="28" height="28" viewBox="0 0 28 28"><circle cx="14" cy="14" r="12.5" fill="none" stroke="#fff" stroke-width="2"/><path d="M10.5 11a3.5 3.5 0 1 1 5 3.2c-1 .5-1.5 1.2-1.5 2.3v.8" fill="none" stroke="#fff" stroke-width="2"/><circle cx="14" cy="20.5" r="1.3" fill="#fff"/></svg>
    </div>
    <div class="user-menu">Dana Orlow &#9652;</div>
  </header>

  <nav class="sidebar">
    <div class="nav-item" style="top:55px"><svg width="22" height="18" viewBox="0 0 22 18"><circle cx="8" cy="5" r="4" fill="none" stroke="#fff" stroke-width="1.3"/><path d="M1 17c0-4 3-6 7-6s7 2 7 6Z" fill="none" stroke="#fff" stroke-width="1.3"/><path d="M13 1.5a4 4 0 0 1 0 7.5M16 11c3 .5 5 2.5 5 6" fill="none" stroke="#fff" stroke-width="1.3"/></svg><span class="label">Users</span></div>
    <div class="nav-item sub" style="top:93px"><span class="label">Roles</span></div>
    <div class="nav-item sub" style="top:133px"><span class="label">Notification Groups</span></div>
    <div class="nav-item active" style="top:177px"><svg width="20" height="20" viewBox="0 0 20 20"><ellipse cx="10" cy="4" rx="8" ry="3" fill="#e9b949"/><path d="M2 6.5c0 1.7 3.6 3 8 3s8-1.3 8-3V9c0 1.7-3.6 3-8 3S2 10.7 2 9Z M2 11.5c0 1.7 3.6 3 8 3s8-1.3 8-3V14c0 1.7-3.6 3-8 3S2 15.7 2 14Z" fill="#e9b949"/></svg><span class="label">Data Sources</span></div>
    <div class="nav-item sub-icon" style="top:220px"><svg width="20" height="20" viewBox="0 0 20 20"><g fill="#fff"><rect x="1" y="1" width="7" height="5"/><rect x="1" y="8" width="7" height="5"/><rect x="1" y="15" width="7" height="4"/><rect x="11" y="3" width="8" height="6"/><rect x="11" y="12" width="8" height="6"/></g></svg><span class="label">Data Object Relationships</span></div>
    <div class="nav-item" style="top:260px"><svg width="22" height="16" viewBox="0 0 22 16"><g fill="none" stroke="#fff" stroke-width="1.4"><path d="M1 2h8M12 2h9M1 8h8M12 8h9M1 14h8M12 14h9"/></g></svg><span class="label">Data Sets</span></div>
    <div class="nav-item" style="top:292px"><svg width="22" height="16" viewBox="0 0 22 16"><g stroke="#fff" stroke-width="1.6"><path d="M1 2h20M6 6h15M9 10h12M1 14h20"/></g></svg><span class="label">Rule Sets</span></div>
    <div class="nav-item" style="top:334px"><svg width="20" height="20" viewBox="0 0 20 20"><circle cx="10" cy="10" r="9" fill="#fff"/><path d="M10 10V4M10 10L6 13" stroke="#2b3342" stroke-width="2"/></svg><span class="label">Schedules</span></div>
    <div class="nav-item hover" style="top:378px"><svg width="22" height="16" viewBox="0 0 22 16"><g fill="none" stroke="#fff" stroke-width="1.6"><path d="M3 6V3h14M14 0.5 L17.5 3 L14 5.5"/><path d="M19 10v3H5M8 10.5 L4.5 13 L8 15.5"/></g></svg><span class="label">Metadata import/Export</span></div>
    <div class="nav-item sub" style="top:417px"><span class="label">Import</span></div>
    <div class="nav-item sub" style="top:450px"><span class="label">Export</span></div>
  </nav>
  <svg class="cursor" width="18" height="28" viewBox="0 0 18 28"><path d="M1 1 L1 22 L6 17 L10 26 L13 24.5 L9 16 L16 16Z" fill="#111" stroke="#fff" stroke-width="1"/></svg>

  <h1 class="page-title">Data Sources</h1>
  <div class="search"><div class="search-btn"><svg width="14" height="14" viewBox="0 0 14 14"><circle cx="6" cy="6" r="4.5" fill="none" stroke="#1b2a40" stroke-width="1.4"/><path d="M9.3 9.3 L13 13" stroke="#1b2a40" stroke-width="1.6"/></svg></div></div>

  <section class="panel">
    <div class="block" style="left:0;top:0;width:770px;height:162px">
      <div class="band" style="padding-left:39px">Data Sources <span class="add-btn">Add</span></div>
      <div class="col-head ds-grid">
        <div></div><div style="border-left:0;padding-left:0">Data Source Name &#9652;</div><div>Type &#8661;</div><div>Status &#8661;</div><div>Actions</div>
      </div>
      <div class="row ds-grid"><div class="exp"><svg width="14" height="14"><use href="#i-expand"/></svg></div><div class="nb" style="padding-left:0">Rowbase</div><div></div><div style="padding-left:19px">Active</div><div class="act"><svg width="18" height="15"><use href="#i-edit"/></svg><svg width="18" height="15"><use href="#i-edit"/></svg><svg width="18" height="15" style="margin-left:8px"><use href="#i-edit"/></svg><svg width="10" height="12" style="margin-left:14px"><use href="#i-trash"/></svg></div></div>
      <div class="row ds-grid zebra"><div class="exp"><svg width="14" height="14"><use href="#i-expand"/></svg></div><div class="nb" style="padding-left:0">Skyledger - Sanbox</div><div style="padding-left:14px">skyledger.com</div><div style="padding-left:19px">Active</div><div class="act"><svg width="18" height="15"><use href="#i-edit"/></svg><svg width="18" height="15"><use href="#i-edit"/></svg><svg width="18" height="15" style="margin-left:8px"><use href="#i-edit"/></svg><svg width="10" height="12" style="margin-left:14px"><use href="#i-trash"/></svg></div></div>
      <div class="row ds-grid"><div class="exp"><svg width="14" height="14"><use href="#i-expand"/></svg></div><div class="nb" style="padding-left:0">SKLD</div><div style="padding-left:14px">skyledger.com</div><div style="padding-left:19px">Active</div><div class="act"><svg width="18" height="15"><use href="#i-edit"/></svg><svg width="18" height="15"><use href="#i-edit"/></svg><svg width="18" height="15" style="margin-left:8px"><use href="#i-edit"/></svg><svg width="10" height="12" style="margin-left:14px"><use href="#i-trash"/></svg></div></div>
      <div class="row ds-grid zebra"><div class="exp"><svg width="14" height="14"><use href="#i-collapse"/></svg></div><div class="nb" style="padding-left:0">skld 44</div><div style="padding-left:14px">skyledger.com</div><div style="padding-left:19px">Active</div><div class="act"><svg width="18" height="15"><use href="#i-edit"/></svg><svg width="18" height="15"><use href="#i-edit"/></svg><svg width="18" height="15" style="margin-left:8px"><use href="#i-edit"/></svg><svg width="10" height="12" style="margin-left:14px"><use href="#i-trash"/></svg></div></div>
    </div>

    <div class="block" style="left:33px;top:162px;width:737px;height:428px">
      <div class="band" style="height:39px;padding-left:37px">Data Objects <span class="add-btn">Add</span></div>
      <div class="col-head" style="grid-template-columns:682px 55px;height:27px"><div style="padding-left:37px">Data Object Name</div><div style="padding-left:8px">Actions</div></div>
      <div class="row do-grid" style="height:23px"><div class="exp"><svg width="14" height="14"><use href="#i-collapse"/></svg></div><div class="nb count" style="padding-left:4px;justify-content:space-between"><span>Account</span><span>28 fields</span></div><div></div></div>

      <div style="position:absolute;left:34px;top:89px;width:703px">
        <div class="band" style="height:37px;padding-left:13px">Fields <span class="add-btn" style="margin-left:22px">Add</span></div>
        <div class="col-head fl-grid"><div>Field Name</div><div>Data Type</div><div>Primary Key</div><div>Rule Types</div><div style="padding-left:6px">Actions</div></div>
        <div class="row fl-grid"><div>Account</div><div>Account</div><div class="pk"><span class="checkbox"><svg width="10" height="10" viewBox="0 0 12 12"><use href="#i-tick"/></svg></span></div><div class="rule-icons"><svg width="16" height="14"><use href="#i-at"/></svg><svg width="14" height="14"><use href="#i-search"/></svg><svg width="14" height="14"><use href="#i-copy"/></svg><svg width="14" height="14"><use href="#i-fork"/></svg><svg width="14" height="14"><use href="#i-globe"/></svg><svg width="14" height="14"><use href="#i-list"/></svg></div><div class="act" style="gap:14px;padding-right:5px"><svg width="18" height="15"><use href="#i-edit"/></svg><svg width="10" height="12"><use href="#i-trash"/></svg></div></div>
        <div class="row fl-grid zebra"><div>Account</div><div>Account</div><div class="pk"><span class="checkbox"></span></div><div class="rule-icons"><svg width="16" height="14"><use href="#i-at"/></svg><svg width="14" height="14"><use href="#i-search"/></svg><svg width="14" height="14"><use href="#i-copy"/></svg><svg width="14" height="14"><use href="#i-fork"/></svg><svg width="14" height="14"><use href="#i-globe"/></svg><svg width="14" height="14"><use href="#i-list"/></svg></div><div class="act" style="gap:14px;padding-right:5px"><svg width="18" height="15"><use href="#i-edit"/></svg><svg width="10" height="12"><use href="#i-trash"/></svg></div></div>
        <div class="row fl-grid"><div>Account</div><div>Account</div><div class="pk"><span class="checkbox"></span></div><div class="rule-icons"><svg width="16" height="14"><use href="#i-at"/></svg><svg width="14" height="14"><use href="#i-search"/></svg><svg width="14" height="14"><use href="#i-copy"/></svg><svg width="14" height="14"><use href="#i-fork"/></svg><svg width="14" height="14"><use href="#i-globe"/></svg><svg width="14" height="14"><use href="#i-list"/></svg></div><div class="act" style="gap:14px;padding-right:5px"><svg width="18" height="15"><use href="#i-edit"/></svg><svg width="10" height="12"><use href="#i-trash"/></svg></div></div>
        <div class="row fl-grid zebra"><div>Account</div><div>Account</div><div class="pk"><span class="checkbox"></span></div><div class="rule-icons"><svg width="16" height="14"><use href="#i-at"/></svg><svg width="14" height="14"><use href="#i-search"/></svg><svg width="14" height="14"><use href="#i-copy"/></svg><svg width="14" height="14"><use href="#i-fork"/></svg><svg width="14" height="14"><use href="#i-globe"/></svg><svg width="14" height="14"><use href="#i-list"/></svg></div><div class="act" style="gap:14px;padding-right:5px"><svg width="18" height="15"><use href="#i-edit"/></svg><svg width="10" height="12"><use href="#i-trash"/></svg></div></div>
        <div class="row fl-grid"><div>Account</div><div>Account</div><div class="pk"><span class="checkbox"></span></div><div class="rule-icons"><svg width="16" height="14"><use href="#i-at"/></svg><svg width="14" height="14"><use href="#i-search"/></svg><svg width="14" height="14"><use href="#i-copy"/></svg><svg width="14" height="14"><use href="#i-fork"/></svg><svg width="14" height="14"><use href="#i-globe"/></svg><svg width="14" height="14"><use href="#i-list"/></svg></div><div class="act" style="gap:14px;padding-right:5px"><svg width="18" height="15"><use href="#i-edit"/></svg><svg width="10" height="12"><use href="#i-trash"/></svg></div></div>
        <div class="row fl-grid zebra"><div>Account</div><div>Account</div><div class="pk"><span class="checkbox"></span></div><div class="rule-icons"><svg width="16" height="14"><use href="#i-at"/></svg><svg width="14" height="14"><use href="#i-search"/></svg><svg width="14" height="14"><use href="#i-copy"/></svg><svg width="14" height="14"><use href="#i-fork"/></svg><svg width="14" height="14"><use href="#i-globe"/></svg><svg width="14" height="14"><use href="#i-list"/></svg></div><div class="act" style="gap:14px;padding-right:5px"><svg width="18" height="15"><use href="#i-edit"/></svg><svg width="10" height="12"><use href="#i-trash"/></svg></div></div>
        <div class="row fl-grid"><div>Account</div><div>Account</div><div class="pk"><span class="checkbox"></span></div><div class="rule-icons"><svg width="16" height="14"><use href="#i-at"/></svg><svg width="14" height="14"><use href="#i-search"/></svg><svg width="14" height="14"><use href="#i-copy"/></svg><svg width="14" height="14"><use href="#i-fork"/></svg><svg width="14" height="14"><use href="#i-globe"/></svg><svg width="14" height="14"><use href="#i-list"/></svg></div><div class="act" style="gap:14px;padding-right:5px"><svg width="18" height="15"><use href="#i-edit"/></svg><svg width="10" height="12"><use href="#i-trash"/></svg></div></div>
        <div class="row fl-grid zebra"><div>Account</div><div>Account</div><div class="pk"><span class="checkbox"></span></div><div class="rule-icons"><svg width="16" height="14"><use href="#i-at"/></svg><svg width="14" height="14"><use href="#i-search"/></svg><svg width="14" height="14"><use href="#i-copy"/></svg><svg width="14" height="14"><use href="#i-fork"/></svg><svg width="14" height="14"><use href="#i-globe"/></svg><svg width="14" height="14"><use href="#i-list"/></svg></div><div class="act" style="gap:14px;padding-right:5px"><svg width="18" height="15"><use href="#i-edit"/></svg><svg width="10" height="12"><use href="#i-trash"/></svg></div></div>
        <div class="row fl-grid"><div>Account</div><div>Account</div><div class="pk"><span class="checkbox"></span></div><div class="rule-icons"><svg width="16" height="14"><use href="#i-at"/></svg><svg width="14" height="14"><use href="#i-search"/></svg><svg width="14" height="14"><use href="#i-copy"/></svg><svg width="14" height="14"><use href="#i-fork"/></svg><svg width="14" height="14"><use href="#i-globe"/></svg><svg width="14" height="14"><use href="#i-list"/></svg></div><div class="act" style="gap:14px;padding-right:5px"><svg width="18" height="15"><use href="#i-edit"/></svg><svg width="10" height="12"><use href="#i-trash"/></svg></div></div>
      </div>

      <div style="position:absolute;left:0;top:383px;width:737px">
        <div class="row" style="grid-template-columns:38px 613px 86px;height:22px"><div class="exp"><svg width="14" height="14"><use href="#i-expand"/></svg></div><div class="nb count" style="justify-content:space-between;padding-left:4px"><span>Contact</span><span>26 fields</span></div><div class="nb exp" style="justify-content:flex-start;padding-left:18px"><svg width="10" height="12"><use href="#i-trash"/></svg></div></div>
        <div class="row zebra" style="grid-template-columns:38px 613px 86px;height:23px"><div class="exp"><svg width="14" height="14"><use href="#i-expand"/></svg></div><div class="nb count" style="justify-content:space-between;padding-left:4px"><span>Lead</span><span>17 fields</span></div><div class="nb exp" style="justify-content:flex-start;padding-left:18px"><svg width="10" height="12"><use href="#i-trash"/></svg></div></div>
      </div>
    </div>

    <div class="block" style="left:0;top:590px;width:770px;height:49px">
      <div class="row" style="grid-template-columns:32px 180px 182px 254px 122px;height:24.5px"><div class="exp"><svg width="14" height="14"><use href="#i-expand"/></svg></div><div class="nb" style="padding-left:7px">Account</div><div>Skyledger.com</div><div>Active</div><div class="act"><svg width="18" height="15"><use href="#i-edit"/></svg><svg width="18" height="15" style="margin-left:6px"><use href="#i-edit"/></svg><svg width="10" height="12"><use href="#i-trash"/></svg></div></div>
      <div class="row zebra" style="grid-template-columns:32px 180px 182px 254px 122px;height:24.5px"><div class="exp"><svg width="14" height="14"><use href="#i-expand"/></svg></div><div class="nb" style="padding-left:7px">Account</div><div>Skyledger.com</div><div>Active</div><div class="act"><svg width="18" height="15"><use href="#i-edit"/></svg><svg width="18" height="15" style="margin-left:6px"><use href="#i-edit"/></svg><svg width="10" height="12"><use href="#i-trash"/></svg></div></div>
    </div>

    <footer class="footer">
      <div class="records">6 of 6 records <span class="page-size">20 <span style="color:#d9a636">&#9662;</span></span></div>
      <div class="pager">
        <svg width="14" height="10" viewBox="0 0 14 10"><path d="M7 0 L0 5 L7 10Z M14 0 L7 5 L14 10Z" fill="#d9a636"/></svg>
        <svg width="7" height="10" viewBox="0 0 7 10"><path d="M7 0 L0 5 L7 10Z" fill="#d9a636"/></svg>
        <div class="page-num">1</div>
        <svg width="7" height="10" viewBox="0 0 7 10"><path d="M0 0 L7 5 L0 10Z" fill="#d9a636"/></svg>
        <svg width="14" height="10" viewBox="0 0 14 10"><path d="M0 0 L7 5 L0 10Z M7 0 L14 5 L7 10Z" fill="#d9a636"/></svg>
      </div>
    </footer>
  </section>
</div>
</body>
</html>
```